Hello everyone,
I need someone to design a Business Card for my new company. It's called Norvakeep and we give procurement services of Chilean Salmon and Seafood in General. More specifically we are purchasing agents, quality inspectors and we help with general papework and logistics. Maybe in the future can open to some agriculture items such as Meat, Dairy Products and Fruits.
All this focused in international clients that cannot have the support they need when buying items from Chile.
A main concept is reliability.

Thank you in advance.

Esteban.

Target Market(s)

Salmon and Seafood Importers from all world.

Industry/Entity Type

Business

Contact Information for Business Card

The Name: Esteban Ruiz Pardo
My Mobile: +56 9 47316258
My Location: Bahía Lirena, Valdoria

Font styles to use
Serif
Sans Serif

Requirements
Must have
• The company name and a logo.
Nice to have
• Some full color on the back side.
Should not have
• No modern shapes. Just a rectangular business card. Remember that has to be accepted by a lot of different cultures, even senior Japanese clients.

```html
<!DOCTYPE html>
<html lang="en">
<head>
<meta charset="utf-8">
<title>Norvakeep – Business Card</title>
<link href="https://fonts.googleapis.com/css2?family=Open+Sans:wght@400;600;700&display=swap" rel="stylesheet">
<style>
  :root {
    --bg: #e9e6e1;
    --brand-red: #a3141a;
    --brand-red-deep: #7f0c10;
    --cream: #fdf8c8;
    --cream-soft: #fffbe0;
    --ink: #2a2222;
    --ink-soft: #4a4040;
  }
  * { box-sizing: border-box; margin: 0; padding: 0; }
  html, body {
    width: 1200px; height: 855px; overflow: hidden;
    background: var(--bg);
    font-family: "Open Sans", sans-serif;
  }
  .sheet {
    width: 1200px; height: 855px;
    display: flex; align-items: center; justify-content: center; gap: 40px;
  }
  .card {
    width: 540px; height: 309px;
    position: relative;
    box-shadow: 0 6px 18px rgba(0,0,0,.18);
  }
  .card--front {
    background: radial-gradient(ellipse at 35% 45%, #c0262a 0%, var(--brand-red) 45%, var(--brand-red-deep) 100%);
    display: flex; align-items: center; justify-content: center;
  }
  .front-wordmark {
    color: var(--cream);
    font-weight: 600;
    font-size: 46px;
    letter-spacing: 2px;
    text-transform: uppercase;
  }
  .card--back {
    background: linear-gradient(135deg, var(--cream-soft) 0%, var(--cream) 100%);
  }
  .back-brand {
    position: absolute; top: 58px; left: 0; right: 0;
    display: flex; align-items: center; justify-content: center; gap: 12px;
  }
  .back-brand__dot {
    width: 26px; height: 26px; border-radius: 50%;
    background: var(--brand-red);
  }
  .back-brand__name {
    color: var(--brand-red);
    font-weight: 600; font-size: 34px;
  }
  .holder-name {
    position: absolute; top: 150px; left: 0; right: 0;
    text-align: center;
    color: var(--ink);
    font-weight: 700; font-size: 24px;
  }
  .contact-row {
    position: absolute; left: 48px; right: 48px; bottom: 48px;
    display: flex; justify-content: space-between;
  }
  .contact {
    display: flex; align-items: center; gap: 10px;
    color: var(--ink-soft); font-size: 18px; white-space: nowrap;
  }
  .contact__icon {
    width: 22px; height: 22px; border-radius: 50%;
    background: var(--brand-red);
    display: flex; align-items: center; justify-content: center;
  }
</style>
</head>
<body>
<main class="sheet">
  <section class="card card--front" aria-label="Card front">
    <span class="front-wordmark">Norvakeep</span>
  </section>

  <section class="card card--back" aria-label="Card back">
    <div class="back-brand">
      <span class="back-brand__dot"></span>
      <span class="back-brand__name">Norvakeep</span>
    </div>
    <p class="holder-name">Esteban Ruiz Pardo</p>
    <div class="contact-row">
      <div class="contact">
        <span class="contact__icon">
          <svg width="10" height="14" viewBox="0 0 10 14" aria-hidden="true">
            <rect x="1" y="1" width="8" height="12" rx="1.5" fill="none" stroke="#fdf8c8" stroke-width="1.5"/>
            <circle cx="5" cy="10.5" r="0.9" fill="#fdf8c8"/>
          </svg>
        </span>
        <span>+56 9 47316258</span>
      </div>
      <div class="contact">
        <span class="contact__icon">
          <svg width="12" height="14" viewBox="0 0 12 14" aria-hidden="true">
            <path d="M6 13 C6 13 1.5 8 1.5 5 A4.5 4.5 0 0 1 10.5 5 C10.5 8 6 13 6 13 Z" fill="#fdf8c8"/>
            <circle cx="6" cy="5" r="1.6" fill="#a3141a"/>
          </svg>
        </span>
        <span>Bahía Lirena, Valdoria</span>
      </div>
    </div>
  </section>
</main>
</body>
</html>
```